property maintenance company covering all trades Plumbing,heating ,electrical building carpentry

business cards

Target Market(s)

DOMESTIC HOUSEHOLDS

Industry/Entity Type

Property Maintenance

Contact Information for Business Card

dorian Pellow
07815 390461
Bramwick Property Maintenace

Font styles to use
Sans Serif

Colors
eda3c7
d2a4cc
b7a5cd

```html
<!DOCTYPE html>
<html lang="en">
<head>
<meta charset="utf-8">
<title>Bramwick Property Maintenace – Business Cards</title>
<link rel="stylesheet" href="https://fonts.googleapis.com/css2?family=Lato:wght@400;700;900&display=swap">
<style>
  :root {
    --page-bg: #e9e9eb;
    --card-bg: #ffffff;
    --brand-blue: #2aa8df;
    --brand-pink: #eda3c7;
    --brand-lilac: #b7a5cd;
    --ink: #222428;
    --rule: #1d1d1f;
  }
  * { box-sizing: border-box; margin: 0; padding: 0; }
  html, body {
    width: 1200px; height: 997px; overflow: hidden;
    background: var(--page-bg);
    font-family: "Lato", Arial, sans-serif;
  }
  .canvas { position: relative; width: 1200px; height: 997px; }

  .card {
    position: absolute;
    width: 540px; height: 310px;
    background: var(--card-bg);
    border-radius: 22px;
    box-shadow: 0 10px 30px rgba(0,0,0,.12);
    overflow: hidden;
  }

  /* Front card */
  .card--front { left: 70px; top: 110px; }
  .card--front .brand {
    position: absolute; left: 0; right: 0; top: 0; bottom: 0;
    display: flex; flex-direction: column; align-items: center; justify-content: center; gap: 18px;
  }
  .brand-dot {
    width: 64px; height: 64px; border-radius: 50%;
    background: var(--brand-blue);
  }
  .brand-name {
    font-weight: 900; color: var(--brand-blue);
    font-size: 30px; letter-spacing: .2px; white-space: nowrap;
  }

  /* Back card */
  .card--back { left: 590px; top: 520px; }
  .card--back .brand {
    position: absolute; left: 0; right: 0; top: 28px;
    display: flex; flex-direction: column; align-items: center; gap: 10px;
  }
  .card--back .brand-dot { width: 44px; height: 44px; }
  .card--back .brand-name { font-size: 21px; }

  .watermark-disc {
    position: absolute; right: 40px; top: 130px;
    width: 110px; height: 110px; border-radius: 50%;
    background: var(--brand-lilac); opacity: .45;
  }
  .top-rule {
    position: absolute; left: 270px; right: 30px; top: 142px;
    height: 1.5px; background: var(--rule);
  }

  .person { position: absolute; left: 34px; top: 168px; right: 180px; }
  .person-name {
    font-weight: 700; color: var(--brand-blue);
    font-size: 17px; letter-spacing: .5px; text-transform: uppercase;
  }
  .person-role {
    display: flex; align-items: center; gap: 6px;
    font-weight: 700; color: var(--ink); font-size: 12px; letter-spacing: .4px;
    margin-top: 2px;
  }
  .person-role::after { content: ""; flex: 1; height: 1.5px; background: var(--rule); }

  .contacts { position: absolute; left: 34px; top: 236px; list-style: none; }
  .contacts li {
    display: flex; align-items: center; gap: 16px;
    font-size: 15px; color: var(--ink); margin-bottom: 12px; letter-spacing: .3px;
  }
  .contact-icon {
    width: 18px; height: 18px; border-radius: 50%;
    background: var(--brand-blue);
    display: flex; align-items: center; justify-content: center; flex: none;
  }
</style>
</head>
<body>
<main class="canvas">

  <section class="card card--front" aria-label="Business card front">
    <div class="brand">
      <span class="brand-dot"></span>
      <span class="brand-name">Bramwick Property Maintenace</span>
    </div>
  </section>

  <section class="card card--back" aria-label="Business card back">
    <div class="brand">
      <span class="brand-dot"></span>
      <span class="brand-name">Bramwick Property Maintenace</span>
    </div>
    <span class="top-rule"></span>
    <span class="watermark-disc"></span>

    <div class="person">
      <p class="person-name">Dorian Pellow</p>
      <p class="person-role">FOUNDER &amp; CEO</p>
    </div>

    <ul class="contacts">
      <li>
        <span class="contact-icon">
          <svg width="10" height="10" viewBox="0 0 10 10"><path d="M5 1 L9 5 H7.6 V9 H2.4 V5 H1 Z" fill="#fff"/></svg>
        </span>
        07815 390461
      </li>
      <li>
        <span class="contact-icon">
          <svg width="10" height="10" viewBox="0 0 10 10"><path d="M5 9.5 C3 6.6 2 5.2 2 3.8 A3 3 0 0 1 8 3.8 C8 5.2 7 6.6 5 9.5 Z" fill="#fff"/><circle cx="5" cy="3.8" r="1.1" fill="#2aa8df"/></svg>
        </span>
        Bramwick Property Maintenace
      </li>
    </ul>
  </section>

</main>
</body>
</html>
```